International Food Company needs packaging design for new products

We have a logo for our new business. It is attached. Now we need a packaging design for the products that we will be selling. We are an international wholesale foods company selling foods and herbs that will be certified organic and Non-GMO imported from West Africa. We are just in the process of launching new products. We're looking for a design that is fresh and modern.

Here is a list of items that we are requesting packaging design for.

Baobob Powder-8 oz and 12 oz
Dried Mango- 8 oz
Mango Powder 8 oz and 12 oz

```html
<!DOCTYPE html>
<html lang="en">
<head>
<meta charset="utf-8">
<title>Baobob Powder Label</title>
<link rel="stylesheet" href="https://fonts.googleapis.com/css2?family=Montserrat:wght@300;400;500&family=Kaushan+Script&display=swap">
<style>
  :root {
    --backdrop: #ececec;
    --brand-green: #046a3a;
    --mid-green: #3fae7a;
    --light-green: #7fd1aa;
    --pale-green: #b9e8cf;
    --brand-text: #2fae72;
    --label-white: #ffffff;
    --ink: #111111;
  }
  * { box-sizing: border-box; margin: 0; padding: 0; }
  html, body {
    width: 1200px;
    height: 900px;
    overflow: hidden;
    background: var(--backdrop);
  }
  .canvas {
    position: relative;
    width: 1200px;
    height: 900px;
  }
  .label {
    position: absolute;
    left: 392px;
    top: 113px;
    width: 418px;
    height: 675px;
    border-radius: 26px;
    overflow: hidden;
    background: var(--label-white);
  }
  .label__band {
    position: absolute;
    left: 0; top: 0;
    width: 100%;
    height: 42px;
    background: var(--brand-green);
    color: var(--label-white);
    font-family: "Montserrat", sans-serif;
    font-weight: 400;
    font-size: 24px;
    letter-spacing: 9px;
    text-align: center;
    line-height: 42px;
    padding-left: 9px;
  }
  .label__artwork {
    position: absolute;
    left: 0; top: 42px;
    width: 100%;
    height: 633px;
  }
  .label__seal {
    position: absolute;
    left: 342px;
    top: 113px;
    width: 364px;
    height: 364px;
    left: 30px;
    top: 139px;
    border-radius: 50%;
    background: var(--label-white);
    text-align: center;
  }
  .brand-name {
    position: absolute;
    left: 0; right: 0;
    top: 76px;
    font-family: "Montserrat", sans-serif;
    font-weight: 300;
    font-size: 30px;
    line-height: 1;
    color: var(--brand-text);
    letter-spacing: 1px;
  }
  .product-name {
    position: absolute;
    left: 0; right: 0;
    font-family: "Kaushan Script", cursive;
    color: var(--brand-green);
    line-height: 1;
    transform: rotate(-9deg);
  }
  .product-name--main {
    top: 150px;
    font-size: 96px;
  }
  .product-name--sub {
    top: 262px;
    left: 40px;
    font-size: 56px;
  }
  .gmo-badge {
    position: absolute;
    left: 19px;
    top: 557px;
  }
  .net-weight {
    position: absolute;
    right: 18px;
    top: 580px;
    font-family: "Montserrat", sans-serif;
    font-weight: 500;
    font-size: 20px;
    line-height: 26px;
    color: var(--ink);
    text-align: right;
  }
</style>
</head>
<body>
  <main class="canvas">
    <section class="label">
      <div class="label__band">100% NATURAL</div>

      <svg class="label__artwork" width="418" height="633" viewBox="0 0 418 633" role="img" aria-label="Green watercolour silhouette of a baobab tree filling the label">
        <defs>
          <radialGradient id="canopy-wash" cx="50%" cy="40%" r="65%">
            <stop offset="0%" stop-color="var(--light-green)"/>
            <stop offset="60%" stop-color="var(--mid-green)"/>
            <stop offset="100%" stop-color="var(--pale-green)"/>
          </radialGradient>
        </defs>
        <rect width="418" height="633" fill="url(#canopy-wash)"/>
      </svg>

      <div class="label__seal">
        <div class="brand-name">SUNFIELD HERBS</div>
        <div class="product-name product-name--main">Baobob</div>
        <div class="product-name product-name--sub">Powder</div>
      </div>

      <svg class="gmo-badge" width="84" height="84" viewBox="0 0 84 84" role="img" aria-label="Non-GMO certification badge">
        <circle cx="42" cy="42" r="41" fill="var(--label-white)" stroke="var(--brand-green)" stroke-width="2"/>
        <circle cx="42" cy="42" r="30" fill="var(--brand-green)"/>
      </svg>

      <div class="net-weight">Net Wt.<br>8 oz</div>
    </section>
  </main>
</body>
</html>
```